CD Cover Design Project

Don't have a huge brief or visual idea of exactly what i want, but here are the details:

Band Name: The Brinewhistles
Title: Most of Where We Ought to Go
Genre: indie rock - think Carried On Lanterns, Drubb, Tarvy, The Plonts, etc)

Definitely want the name and title on the cover. It could be more photography based or design based. A little more abstract. Totally open. Brinewhistles chew up everything they see... One thought was an eaten, old beat up guitar...maybe too cliche.

Album covers i love: Allwhiles, Marble Sleeping, Sidestep the Pebbles, Dusty Ladders, Make me Drift

Happy to send music or give feedback on concepts prior to working on them...not sure of the rules...whatever is within them.

```html
<!DOCTYPE html>
<html lang="en">
<head>
<meta charset="utf-8">
<title>The Brinewhistles — Most of Where We Ought to Go — Disc Label</title>
<link rel="stylesheet" href="https://fonts.googleapis.com/css2?family=Pinyon+Script&display=swap">
<style>
  :root {
    --page: #ffffff;
    --disc-deep: #1e1a33;
    --disc-mid: #2f2848;
    --disc-violet: #4a3560;
    --disc-warm: #6b4a68;
    --disc-slate: #3a3a48;
    --band-top: rgba(214, 212, 214, 0.72);
    --band-bottom: rgba(226, 220, 236, 0.88);
    --title-light: #f1efe6;
    --title-dark: #2a2433;
  }
  html, body {
    margin: 0;
    padding: 0;
    width: 1200px;
    height: 1200px;
    overflow: hidden;
    background: var(--page);
  }
  .disc-label {
    display: block;
    width: 1200px;
    height: 1200px;
  }
  .band-name {
    font-family: "Pinyon Script", cursive;
    font-size: 108px;
    fill: var(--title-light);
  }
  .album-title {
    font-family: "Pinyon Script", cursive;
    font-size: 74px;
    fill: var(--title-dark);
  }
</style>
</head>
<body>
<svg class="disc-label" viewBox="0 0 1200 1200" xmlns="http://www.w3.org/2000/svg">
  <defs>
    <radialGradient id="disc-photo-tone" cx="0.42" cy="0.38" r="0.75">
      <stop offset="0" stop-color="var(--disc-warm)"/>
      <stop offset="0.35" stop-color="var(--disc-violet)"/>
      <stop offset="0.7" stop-color="var(--disc-mid)"/>
      <stop offset="1" stop-color="var(--disc-slate)"/>
    </radialGradient>
    <linearGradient id="disc-shade" x1="0" y1="0" x2="1" y2="1">
      <stop offset="0" stop-color="#000" stop-opacity="0.15"/>
      <stop offset="0.6" stop-color="#000" stop-opacity="0"/>
      <stop offset="1" stop-color="var(--disc-deep)" stop-opacity="0.55"/>
    </linearGradient>
    <mask id="disc-hole">
      <rect width="1200" height="1200" fill="#fff"/>
      <circle cx="600" cy="600" r="191" fill="#000"/>
    </mask>
    <clipPath id="disc-clip">
      <circle cx="600" cy="600" r="600"/>
    </clipPath>
  </defs>

  <g class="disc" mask="url(#disc-hole)">
    <g clip-path="url(#disc-clip)">
      <rect class="disc-photo" role="img"
            aria-label="Dim purple-toned photograph of an acoustic guitar leaning against an amplifier in a practice room"
            width="1200" height="1200" fill="url(#disc-photo-tone)"/>
      <rect width="1200" height="1200" fill="url(#disc-shade)"/>

      <g class="title-band title-band--top">
        <rect x="153" y="142" width="856" height="128" rx="8" fill="var(--band-top)"/>
        <text class="band-name" x="581" y="238" text-anchor="middle">The Brinewhistles</text>
      </g>

      <g class="title-band title-band--bottom">
        <rect x="191" y="810" width="852" height="136" rx="8" fill="var(--band-bottom)"/>
        <text class="album-title" x="617" y="894" text-anchor="middle">Most of Where We Ought to Go</text>
      </g>
    </g>
  </g>
</svg>
</body>
</html>
```